Business Card Design - Service Company

Use of the card mainly in living rooms and relations b2b We wish a card with a modern design, blue tones in the background would be a plus The card must be front / back (one side with the logo / the other with the information of contact )

Font styles to use
Serif

Requirements
Must have
• Using the map on the back of the business card Editable format! Photoshop CS2 / Illustrator CS2
Nice to have
• Maquis Vertex IT Pierre Blanche Commercial Center, 20480 Lorvanu 0495718243 Siret 71384096200018 APE 6203Y https://www.fb.com/ateliertech.maquisvertex www.maquis-vertex.com

```html
<!DOCTYPE html>
<html lang="fr">
<head>
<meta charset="utf-8">
<title>Maquis Vertex IT – Business Card</title>
<link rel="stylesheet" href="https://fonts.googleapis.com/css2?family=Montserrat:wght@600&family=Roboto:wght@400;500;700&display=swap">
<style>
  :root {
    --backdrop: #e3e3e3;
    --card-white: #ffffff;
    --brand-blue: #2a8ccc;
    --ink-dark: #111111;
    --ink-grey: #4a4a4a;
    --rule-grey: #8a8a8a;
  }
  * { margin: 0; padding: 0; box-sizing: border-box; }
  html, body { width: 1125px; height: 1200px; overflow: hidden; }
  body {
    background: var(--backdrop);
    position: relative;
    font-family: "Roboto", Arial, sans-serif;
  }
  .card {
    position: absolute;
    width: 826px;
    height: 471px;
    overflow: hidden;
  }
  .card--front { left: 177px; top: 110px; background: var(--card-white); }
  .card--back  { left: 171px; top: 639px; background: var(--brand-blue); }

  .brand-name {
    font-family: "Montserrat", Arial, sans-serif;
    font-weight: 600;
    white-space: nowrap;
    letter-spacing: 0.5px;
  }
  .card--front .brand-name {
    position: absolute;
    right: 51px;
    top: 133px;
    font-size: 33px;
    color: var(--brand-blue);
  }

  .holder-name {
    position: absolute;
    left: 47px; top: 234px;
    font-size: 31px; font-weight: 700;
    color: var(--brand-blue);
    letter-spacing: 0.3px;
  }
  .holder-role {
    position: absolute;
    left: 47px; top: 268px;
    font-size: 20px; font-weight: 500;
    color: var(--ink-dark);
  }
  .divider {
    position: absolute;
    left: 47px; top: 309px;
    width: 728px; height: 2px;
    background: var(--ink-dark);
  }

  .contact-list {
    position: absolute;
    left: 47px; top: 323px;
    list-style: none;
    font-size: 20px;
    color: var(--ink-grey);
  }
  .contact-list li {
    display: flex; align-items: center;
    height: 26px;
  }
  .contact-list .icon { width: 18px; height: 18px; margin-right: 12px; flex: none; }
  .contact-list .legal { margin-top: 4px; }

  .address {
    position: absolute;
    right: 51px; top: 346px;
    text-align: right;
    font-size: 20px;
    line-height: 25px;
    color: var(--ink-grey);
    font-style: normal;
  }
  .address .company { font-weight: 500; color: #333333; }

  .base-rule {
    position: absolute;
    left: 0; top: 447px;
    width: 100%; height: 3px;
    background: var(--rule-grey);
  }
  .base-band {
    position: absolute;
    left: 0; top: 451px;
    width: 100%; height: 20px;
    background: var(--brand-blue);
  }

  .card--back .brand-name {
    position: absolute;
    left: 44px; top: 322px;
    font-size: 44px;
    color: var(--card-white);
  }
  .card--back .web {
    position: absolute;
    left: 44px; top: 412px;
    font-size: 19px;
    letter-spacing: 4px;
    color: var(--card-white);
  }
</style>
</head>
<body>

  <section class="card card--front" aria-label="Card front, contact details">
    <div class="brand-name">MAQUIS VERTEX IT</div>

    <h1 class="holder-name">PAUL SANTINI</h1>
    <p class="holder-role">CEO/FOUNDER</p>
    <div class="divider"></div>

    <ul class="contact-list">
      <li>
        <svg class="icon" viewBox="0 0 24 24" aria-hidden="true"><path fill="#2a8ccc" d="M6.6 10.8a15.1 15.1 0 0 0 6.6 6.6l2.2-2.2a1 1 0 0 1 1-.25 11.4 11.4 0 0 0 3.6.57 1 1 0 0 1 1 1V20a1 1 0 0 1-1 1A17 17 0 0 1 3 4a1 1 0 0 1 1-1h3.5a1 1 0 0 1 1 1c0 1.25.2 2.45.57 3.6a1 1 0 0 1-.25 1z"/></svg>
        0495718243
      </li>
      <li>
        <svg class="icon" viewBox="0 0 24 24" aria-hidden="true"><rect x="3" y="3" width="18" height="18" fill="#2a8ccc"/></svg>
        @maquisvertex
      </li>
      <li>
        <svg class="icon" viewBox="0 0 24 24" aria-hidden="true"><circle cx="12" cy="12" r="10" fill="#2a8ccc"/><path d="M2 12h20M12 2c3 3 3 17 0 20M12 2c-3 3-3 17 0 20" stroke="#fff" stroke-width="1.5" fill="none"/></svg>
        www.maquis-vertex.com
      </li>
      <li class="legal">Siret 71384096200018 APE 6203Y</li>
    </ul>

    <address class="address">
      <span class="company">MAQUIS VERTEX IT</span><br>
      Centre Commercial<br>
      Pierre Blanche, 20480 Lorvanu
    </address>

    <div class="base-rule"></div>
    <div class="base-band"></div>
  </section>

  <section class="card card--back" aria-label="Card back, brand side">
    <div class="brand-name">MAQUIS VERTEX IT</div>
    <p class="web">www.maquis-vertex.com</p>
  </section>

</body>
</html>
```